Tree Pruning Website

We need a website for a tree Arborist, pruning company called Hollow Ridge Branchworks. We look after all types of trees, knock down trees and prune trees. Our target market is from domestic clients to government clients and everything in between.

We would like to see the use of our main colours which are orange and green

We are not looking forward in seeing a template that we have seen before but a unique template. We have designed 5 templates ourselves and we wish for the design community to take our designs to the next level.

We have also designed a template for things that **we are not** looking for (Version 4)

To make it fair for everyone, we are also not giving out any participation payments as we have had. One winner will take all of the payment!!!

I Have attached a image of the designs and a image of a tree.

We are just looking at the PSD file been developed. We have our own team who can slice the image up into a HTML format.

Target Market(s)

Everyone who needs to cut down a tree

Industry/Entity Type

Government

Requirements
Must have
• Logo on front page
A List of our services
jQuery slider on page
Phone Number on every page

```html
<!DOCTYPE html>
<html lang="en">
<head>
<meta charset="utf-8">
<title>Hollow Ridge Branchworks</title>
<link href="https://fonts.googleapis.com/css2?family=Mulish:wght@400;600;700;800&display=swap" rel="stylesheet">
<style>
:root{
  --page-bg:#5b8a4f;
  --leaf:#6a9a1e;
  --leaf-light:#7fba2a;
  --leaf-dark:#3f6a2e;
  --orange:#f0782a;
  --orange-light:#f8913a;
  --panel:#efefef;
  --ink:#444;
  --text:#4a4a4a;
  --line:#dcdcdc;
  --white:#fff;
}
*{box-sizing:border-box;margin:0;padding:0}
html,body{width:1186px;height:1200px;overflow:hidden}
body{background:var(--page-bg);font-family:"Mulish",sans-serif;color:var(--text);position:relative}
.site{position:absolute;left:169px;top:0;width:847px;height:1127px;background:var(--panel)}
.top-rule{position:absolute;left:0;top:0;width:847px;height:5px;background:var(--leaf-light)}
.header{position:absolute;left:0;top:5px;width:847px;height:88px;background:var(--white)}
.brand{position:absolute;left:18px;top:22px;display:flex;align-items:center;gap:12px}
.brand-dot{width:40px;height:40px;border-radius:50%;background:var(--leaf)}
.brand-name{font-size:21px;font-weight:700;color:var(--leaf);line-height:1.1}
.phone{position:absolute;right:18px;top:18px;display:flex;align-items:center;gap:6px;color:var(--orange);font-size:18px}
.nav{position:absolute;right:18px;top:53px;display:flex;gap:24px;font-size:13.5px;color:#222}
.nav a{color:inherit;text-decoration:none;position:relative;padding-bottom:20px}
.nav a.current{color:var(--orange)}
.nav a.current::after{content:"";position:absolute;left:-5px;right:-5px;bottom:0;height:3px;background:var(--leaf-light)}
.slider{position:absolute;left:0;top:102px;width:847px;height:288px;background:linear-gradient(100deg,#3e6f1c 0%,#5d9a28 40%,#8fc45a 70%,#d7e8c0 100%)}
.slider-photo{position:absolute;inset:0}
.slide-title{position:absolute;left:20px;top:42px;font-size:30px;font-weight:700;color:var(--white);text-shadow:0 1px 3px rgba(0,0,0,.35)}
.slide-text{position:absolute;left:22px;top:90px;width:420px;font-size:14px;line-height:26px;color:var(--white);text-shadow:0 1px 2px rgba(0,0,0,.3)}
.btn{position:absolute;left:23px;top:208px;width:101px;height:41px;border:1px solid #b9e27a;border-radius:4px;background:linear-gradient(#8fd23a,#5aa516);color:#123;font-size:15px;display:flex;align-items:center;justify-content:center}
.dots{position:absolute;left:23px;top:269px;display:flex;gap:6px}
.dots span{width:9px;height:9px;border-radius:50%;background:#3d6a1a}
.dots span.on{background:var(--white)}
.sectors{position:absolute;left:17px;top:422px;width:813px;height:120px;border:1px solid var(--line);border-radius:10px;background:linear-gradient(#f8f8f8,#e6e6e6);display:flex;overflow:hidden}
.sector{flex:1;display:flex;gap:8px;padding:20px 0 0 10px;border-left:1px solid var(--line)}
.sector:first-child{border-left:0}
.sector svg{flex:none;margin-top:22px}
.sector h3{font-size:17px;font-weight:700;color:var(--orange);margin:0 0 6px 12px;white-space:nowrap}
.sector p{font-size:10.5px;line-height:17px;margin-left:12px;width:122px;color:var(--text)}
.sector.active{background:linear-gradient(#f4924e,#fb6a16)}
.sector.active h3,.sector.active p{color:var(--white)}
.heading{position:absolute;display:flex;align-items:center;gap:12px;font-size:18px;font-weight:700;color:var(--ink)}
.heading::before{content:"";width:23px;height:17px;border-radius:5px 9px 9px 5px;background:linear-gradient(var(--orange-light),var(--orange))}
.heading.big{font-size:22px}
.work{position:absolute;top:608px;width:181px;height:109px;border:2px solid var(--leaf-light);border-radius:0 0 0 14px;overflow:hidden;background:var(--leaf)}
.work-photo{height:70px;background:linear-gradient(#9ab3c9,#6d5a3c)}
.work p{padding:4px 11px;font-size:10.5px;line-height:13.5px;color:#f0f6e4}
.welcome{position:absolute;left:17px;top:797px;width:570px;font-size:11px;line-height:17.8px;color:var(--text)}
.welcome p{margin-bottom:17px}
.services{position:absolute;left:608px;top:607px;width:222px;border:1px solid var(--line);list-style:none;background:#ececec}
.services li{height:33.7px;display:flex;align-items:center;gap:14px;padding-left:12px;border-top:1px solid var(--line);font-size:14px;color:var(--leaf)}
.services li:first-child{border-top:0}
.services li::before{content:"";width:8px;height:8px;border-radius:50%;background:var(--leaf)}
.thumb{position:absolute;width:104px;height:74px;border:1px solid #ccc;background:linear-gradient(#4d86c9,#6f6a3e)}
.footer{position:absolute;left:169px;top:1135px;width:847px;height:49px;border:1px solid #2f5725;background:linear-gradient(#4f7f3f,#3b6830);display:flex;align-items:center;justify-content:space-between;padding:0 18px;font-size:10.5px;color:#e4eedd}
.footer nav{display:flex;gap:18px}
</style>
</head>
<body>
<div class="site">
  <div class="top-rule"></div>
  <header class="header">
    <div class="brand"><span class="brand-dot"></span><span class="brand-name">Hollow Ridge<br>Branchworks</span></div>
    <div class="phone">
      <svg width="11" height="20" viewBox="0 0 11 20"><rect x="0.5" y="0.5" width="10" height="19" rx="2" fill="none" stroke="#f0782a"/><rect x="2.5" y="3" width="6" height="8" fill="#f0782a"/><rect x="2.5" y="13" width="6" height="4" fill="#f0782a"/></svg>
      08 5550 0142
    </div>
    <nav class="nav"><a class="current">Home</a><a>About</a><a>Our Services</a><a>Get a Quote</a><a>Contact Us</a></nav>
  </header>

  <section class="slider">
    <div class="slider-photo" role="img" aria-label="Hands holding a young tree with its soil against a green meadow"></div>
    <h1 class="slide-title">Let us take care of your trees !</h1>
    <p class="slide-text">Le Lorem Ipsum est simplement du faux texte employé dans la composition et la mise en page avant impression. Le Lorem Ipsum est le faux texte standard de l'imprimerie depuis les années 1500.</p>
    <div class="btn">Read More</div>
    <div class="dots"><span></span><span class="on"></span><span></span><span></span></div>
  </section>

  <section class="sectors">
    <div class="sector">
      <svg width="48" height="48" viewBox="0 0 52 48"><path d="M26 2 L50 24 H43 V46 H31 V32 H21 V46 H9 V24 H2 Z" fill="#6a9a1e"/><rect x="36" y="6" width="6" height="12" fill="#6a9a1e"/></svg>
      <div><h3>Domestic</h3><p>Le Lorem Ipsum est simplement du faux texte employé dans.</p></div>
    </div>
    <div class="sector active">
      <svg width="48" height="48" viewBox="0 0 46 48"><path d="M20 2 L32 16 H26 L36 28 H28 L40 40 H24 V46 H16 V40 H0 L12 28 H4 L14 16 H8 Z" fill="#fff"/><rect x="16" y="45" width="30" height="2" fill="#fff"/></svg>
      <div><h3>Commercial</h3><p>Le Lorem Ipsum est simplement du faux texte employé dans.</p></div>
    </div>
    <div class="sector">
      <svg width="48" height="48" viewBox="0 0 48 48"><path d="M24 2 L46 14 H2 Z" fill="#6a9a1e"/><rect x="4" y="16" width="40" height="3" fill="#6a9a1e"/><rect x="8" y="21" width="5" height="18" fill="#6a9a1e"/><rect x="17" y="21" width="5" height="18" fill="#6a9a1e"/><rect x="26" y="21" width="5" height="18" fill="#6a9a1e"/><rect x="35" y="21" width="5" height="18" fill="#6a9a1e"/><rect x="2" y="41" width="44" height="5" fill="#6a9a1e"/></svg>
      <div><h3>Government</h3><p>Le Lorem Ipsum est simplement du faux texte employé dans.</p></div>
    </div>
    <div class="sector">
      <svg width="48" height="40" viewBox="0 0 48 40"><path d="M10 36 A9 9 0 0 1 8 18 A12 12 0 0 1 30 10 A10 10 0 0 1 44 22 A8 8 0 0 1 40 36 Z" fill="#6a9a1e"/></svg>
      <div><h3>Non Profit</h3><p>Le Lorem Ipsum est simplement du faux texte employé dans.</p></div>
    </div>
  </section>

  <h2 class="heading" style="left:17px;top:573px">Latest Work</h2>
  <div class="work" style="left:16px"><div class="work-photo" role="img" aria-label="Worker cutting a tree limb from a lift"></div><p>Contrairement à une opinion répandue, le Lorem Ipsum n'est</p></div>
  <div class="work" style="left:211px"><div class="work-photo" role="img" aria-label="Pale branches of a pruned tree"></div><p>Contrairement à une opinion répandue, le Lorem Ipsum n'est</p></div>
  <div class="work" style="left:406px"><div class="work-photo" role="img" aria-label="Climber working in a large tree canopy"></div><p>Contrairement à une opinion répandue, le Lorem Ipsum n'est</p></div>

  <h2 class="heading big" style="left:17px;top:744px">Welcome to Hollow Ridge Branchworks</h2>
  <div class="welcome">
    <p>Le Lorem Ipsum est simplement du faux texte employé dans la composition et la mise en page avant impression. Le Lorem Ipsum est le faux texte standard de l'imprimerie depuis les années 1500, quand un peintre anonyme assembla ensemble des morceaux de texte pour réaliser un livre spécimen de polices de texte. Il n'a pas fait que survivre cinq siècles, mais s'est aussi adapté à la bureautique informatique, sans que son contenu n'en soit modifié.</p>
    <p>Il a été popularisé dans les années 1960 grâce à la vente de feuilles Pressfold contenant des passages du Lorem Ipsum, et, plus récemment, par son inclusion dans des applications de mise en page de texte, comme Quillset Layout.</p>
    <p>Le Lorem Ipsum est simplement du faux texte employé dans la composition et la mise en page avant impression. Le Lorem Ipsum est le faux texte standard de l'imprimerie depuis les années 1500, quand un peintre anonyme assembla ensemble des morceaux de texte pour réaliser un livre spécimen de polices de texte. Il n'a pas fait que survivre cinq siècles, mais s'est aussi adapté à la bureautique informatique, sans que son contenu n'en soit modifié. Il a été popularisé dans les années 1960 grâce à la vente de feuilles Pressfold contenant des passages du Lorem Ipsum, et, plus récemment, par son inclusion dans des applications de mise en page de texte, comme Quillset Layout.</p>
  </div>

  <h2 class="heading" style="left:608px;top:573px">Our Services</h2>
  <ul class="services">
    <li>Diagnosis</li><li>Treatment</li><li>Purning</li><li>Tree Removal</li><li>Stump Removal</li><li>Cabling &amp; Bracing</li><li>Arborist Consult</li><li>Tree Protection</li>
  </ul>

  <h2 class="heading" style="left:608px;top:895px">Image Gallery</h2>
  <div class="thumb" style="left:609px;top:932px" role="img" aria-label="Arborists climbing a tree against blue sky"></div>
  <div class="thumb" style="left:726px;top:932px;background:linear-gradient(#6e7a4a,#5a4630)" role="img" aria-label="Arborist in orange gear on a tree trunk"></div>
  <div class="thumb" style="left:609px;top:1022px" role="img" aria-label="Climber in a palm tree"></div>
  <div class="thumb" style="left:726px;top:1022px;background:linear-gradient(#4d86c9,#a07a40)" role="img" aria-label="Hand pruning a branch with shears"></div>
</div>

<footer class="footer">
  <nav><span>Home</span><span>About</span><span>Our Services</span><span>Get a Quote</span><span>Contact Us</span></nav>
  <span>© Copyrights 2013 All rights Reserved</span>
</footer>
</body>
</html>
```